A New and modern Business Card for Tarvish Commerce Partners Ltd

New and modern Logo and Business Card Attached is the current logo/business card designCurrently the business is called "Tarvish & Co." or TCP Ltd for short. This is subject to change.This business specialises in Telecoms and Energy. We work with the major networks (QX, Z7, etc) and also offer Energy Products saving clients money off their energy bills.These are business to business services.The current design incorporates a Pheonix, indicating rebirth, starting something new.We would like to maintain the Phoenix element but a newer modern style.We love colours in the logo 3 max.The aim of this is to be ultra slick and modern. I envisage Tarvish & Co. on one side of the card with long descriptions on the other side.Side 1:TCP Ltd/Logo?Side 2:TCP Ltd/Logo/Graphic?Brogan & Co.Name:Address:Phone:Email:The design is mostly flexible but must incorporate a Phoenix.For example "Tarvish & Co." with a block phoenix behind the text...up to you.

Industry/Entity Type

Telecommunications

Contact Information for Business Card

Tarvish & Co.
Address:
Name:
Phone:
Email:

Logo Text

Tarvish & Co.

Colors
33a6d7
0792cd
acd037
9bcb3c
f78f20
fece3e

Requirements
Must have
• Phoenix
• 3/4 colours max
• Blue representing Technology (wireless)
• Green for Eco Energy
• Orange for Phoenix
• White business card background
Should not have
• phoenix must not all be red/ orange fire, we are a technology service company and the phoenix colours must represent this. Fire is not representative of our company.

```html
<!DOCTYPE html>
<html lang="en">
<head>
<meta charset="utf-8">
<title>Tarvish Commerce Partners Ltd — Business Card</title>
<link href="https://fonts.googleapis.com/css2?family=Cinzel:wght@400;600&family=Lato:wght@400&display=swap" rel="stylesheet">
<style>
  :root {
    --stage: #e4e6e8;
    --card: #ffffff;
    --card-edge: #d4d7da;
    --blue: #0792cd;
    --blue-light: #33a6d7;
    --green: #9bcb3c;
    --orange: #f78f20;
    --text-dark: #3a3f44;
    --divider: #dde1e4;
  }
  * { margin: 0; padding: 0; box-sizing: border-box; }
  html, body { width: 1200px; height: 844px; overflow: hidden; }
  body {
    background: var(--stage);
    display: flex;
    align-items: center;
    justify-content: center;
    gap: 60px;
    font-family: "Lato", sans-serif;
  }
  .card {
    width: 525px;
    height: 300px;
    background: var(--card);
    border: 1px solid var(--card-edge);
    position: relative;
    overflow: hidden;
  }
  /* Front */
  .card-front { display: flex; }
  .brand-side {
    width: 53%;
    display: flex;
    flex-direction: column;
    align-items: center;
    justify-content: center;
    gap: 16px;
    border-right: 1px solid var(--divider);
  }
  .brand-dot {
    width: 58px; height: 58px;
    border-radius: 50%;
    background: var(--orange);
  }
  .brand-name {
    font-family: "Cinzel", serif;
    font-weight: 600;
    color: var(--blue);
    text-align: center;
    font-size: 14px;
    line-height: 1.35;
    letter-spacing: 0.5px;
    text-transform: uppercase;
  }
  .brand-name .lead { display: block; font-size: 34px; line-height: 1.05; letter-spacing: 1px; }
  .contact-side {
    flex: 1;
    padding: 64px 0 0 28px;
    color: var(--text-dark);
    font-size: 14px;
    line-height: 1.35;
  }
  .person-name {
    font-family: "Cinzel", serif;
    font-weight: 400;
    color: var(--blue);
    font-size: 17px;
    letter-spacing: 0.5px;
  }
  .person-role { margin-bottom: 4px; color: var(--green); }
  .contact-line { display: flex; align-items: center; gap: 7px; }
  .contact-line svg { width: 11px; height: 11px; flex: none; }
  .address { margin-top: 8px; }
  /* Back */
  .card-back {
    display: flex;
    flex-direction: column;
    align-items: center;
    justify-content: center;
    gap: 16px;
  }
  .back-dot {
    width: 70px; height: 70px;
    border-radius: 50%;
    background: var(--orange);
  }
  .back-name {
    font-family: "Cinzel", serif;
    font-weight: 600;
    color: var(--blue);
    font-size: 30px;
    letter-spacing: 2px;
    text-transform: uppercase;
  }
</style>
</head>
<body>
  <section class="card card-front">
    <div class="brand-side">
      <div class="brand-dot"></div>
      <p class="brand-name"><span class="lead">Tarvish</span>Commerce Partners Limited</p>
    </div>
    <div class="contact-side">
      <p class="person-name">MARCUS ELWOOD</p>
      <p class="person-role">Managing Director</p>
      <p class="contact-line">
        <svg viewBox="0 0 12 12" aria-hidden="true"><path fill="#9bcb3c" d="M2.5 1h2l1 2.5-1.2 1a6 6 0 0 0 3.2 3.2l1-1.2L11 7.5v2A1.5 1.5 0 0 1 9.5 11 8.5 8.5 0 0 1 1 2.5 1.5 1.5 0 0 1 2.5 1z"/></svg>
        044-987 650 321
      </p>
      <p class="contact-line">
        <svg viewBox="0 0 12 12" aria-hidden="true"><rect x="1" y="2.5" width="10" height="7" fill="#9bcb3c"/><path d="M1 2.5l5 4 5-4" fill="none" stroke="#ffffff" stroke-width="1"/></svg>
        hello@tarvishco.com
      </p>
      <p class="address">421, Address line here,<br>45452,Country Name</p>
    </div>
  </section>
  <section class="card card-back">
    <div class="back-dot"></div>
    <p class="back-name">Tarvish</p>
  </section>
</body>
</html>
```